ZEV COACH logo & business card needed
i need a new logo & business card
I need double sided Folded Business Card [3.5" x 4"]
use whatever font is clear and would look good
Bright & Fun-filled
Teodoro Villanisti
CEO
47 Pemberly Lane, Suite 6
Brookhaven Falls, NY 14099
tv@zevcoach.com
http://www.ZevCoach.com
make it trendy, legible, and exciting
MENTION THIS BUSINESS CARD AND GET 10% OFF YOUR NEXT BOOKING - USE CODE
TV10%
here are some interior shots of our limo buses that i would like to incorporate as a background for the business card..
more photos
HERE IS OUR LOGO
HERE IS OUR BUSINESS CARD TO GIVE YOU AN IDEA OF THE OVERALL LOOK AND FEEL WE ARE GOING FOR

```html
<!DOCTYPE html>
<html lang="en">
<head>
<meta charset="utf-8">
<title>ZEV COACH Stationery</title>
<link href="https://fonts.googleapis.com/css2?family=Open+Sans:wght@400;600;700;800&display=swap" rel="stylesheet">
<style>
  :root{
    --bg:#e4e6e8;
    --ink:#1b1d20;
    --card-black:#0c0d0f;
    --brand-grey:#6b6f75;
    --brand-blue:#1f8fd6;
    --deep-blue:#123a8c;
    --paper:#ffffff;
    --soft-grey:#d6d8db;
    --text-light:#f2f4f6;
  }
  *{box-sizing:border-box;margin:0;padding:0}
  html,body{width:1200px;height:804px;overflow:hidden}
  body{background:var(--bg);font-family:"Open Sans",Arial,sans-serif;color:var(--ink);position:relative}
  .piece{position:absolute;box-shadow:0 4px 14px rgba(0,0,0,.25)}
  .wordmark{font-weight:800;color:var(--brand-grey);letter-spacing:1px;font-family:"Open Sans",Arial,sans-serif;white-space:nowrap}

  /* card front */
  .card-front{left:67px;top:60px;width:312px;height:168px;background:var(--card-black);border-radius:12px;overflow:hidden;color:var(--text-light)}
  .card-front .bus-photo{position:absolute;left:12px;top:40px;width:130px;height:48px;border-radius:6px;background:linear-gradient(180deg,#f4f4f4,#9ea3a8)}
  .card-front .name{position:absolute;left:16px;top:12px;font-size:10px;font-weight:700}
  .card-front .title{position:absolute;left:16px;top:25px;font-size:8px;color:#b9bdc2}
  .card-front .wordmark{position:absolute;left:156px;width:140px;top:54px;font-size:18px;text-align:right;color:#e9ebee}
  .card-front .rule{position:absolute;left:150px;top:84px;width:146px;height:2px;background:var(--brand-blue)}
  .card-front .contact{position:absolute;left:16px;top:108px;right:16px;font-size:6.5px;line-height:1.7;color:#c9ccd0;display:grid;grid-template-columns:1fr 1fr 1fr;column-gap:6px}
  .card-front .contact .addr{grid-column:1 / 4;text-align:center;margin-bottom:2px}

  /* card back */
  .card-back{left:271px;top:240px;width:298px;height:175px;border-radius:12px;overflow:hidden;background:var(--deep-blue)}
  .card-back .interior-photo{position:absolute;inset:0 0 30px 0;background:radial-gradient(ellipse at 50% 40%,#5a87c4,#1c2f63 70%,#0b1433)}
  .card-back .offer{position:absolute;left:24px;right:24px;top:90px;font-size:10px;font-weight:700;text-align:center;color:#fff;line-height:1.35}
  .card-back .web-band{position:absolute;left:0;right:0;bottom:0;height:30px;background:linear-gradient(90deg,var(--brand-blue),var(--deep-blue));color:#fff;font-size:10px;font-weight:600;text-align:center;line-height:30px}

  /* envelope */
  .envelope{left:67px;top:444px;width:502px;height:300px;background:var(--paper);overflow:hidden}
  .envelope .flap{position:absolute;left:0;top:0;width:100%;height:60px}
  .envelope .wordmark{position:absolute;left:30px;top:82px;font-size:34px}
  .envelope .swoosh{position:absolute;left:0;top:140px;width:100%;height:40px}
  .envelope .address{position:absolute;left:30px;bottom:18px;font-size:8px;color:#4a4d52}

  /* letterhead */
  .letterhead{left:583px;top:60px;width:552px;height:679px;background:var(--paper);overflow:hidden}
  .letterhead .wordmark{position:absolute;left:28px;top:26px;font-size:42px}
  .letterhead .swoosh{position:absolute;left:0;top:92px;width:100%;height:40px}
  .letterhead .interior-photo{position:absolute;left:0;right:0;top:270px;bottom:70px;background:linear-gradient(180deg,rgba(255,255,255,1),rgba(205,210,216,.55) 55%,rgba(255,255,255,1))}
  .letterhead .footer{position:absolute;left:0;right:0;bottom:14px;font-size:9px;color:#4a4d52;text-align:center;line-height:1.9}
  .letterhead .footer span{margin:0 10px}
</style>
</head>
<body>

<section class="piece card-front" aria-label="Business card front">
  <div class="name">Teodoro Villanisti</div>
  <div class="title">CEO</div>
  <div class="bus-photo" role="img" aria-label="Photo of a white limo bus"></div>
  <div class="wordmark">ZEV COACH</div>
  <div class="rule"></div>
  <div class="contact">
    <div class="addr">47 Pemberly Lane, Suite 6, Brookhaven Falls, NY 14099</div>
    <div>716-555-0142</div><div>716-555-0187</div><div>866-555-0193</div>
    <div>tv@zevcoach.com</div><div></div><div>www.ZevCoach.com</div>
  </div>
</section>

<section class="piece card-back" aria-label="Business card back">
  <div class="interior-photo" role="img" aria-label="Photo of a limo bus interior with lights"></div>
  <p class="offer">MENTION THIS BUSINESS CARD AND GET 10% OFF YOUR NEXT BOOKING - USE CODE TV10%</p>
  <div class="web-band">www.ZevCoach.com</div>
</section>

<section class="piece envelope" aria-label="Envelope">
  <svg class="flap" viewBox="0 0 502 60" preserveAspectRatio="none">
    <defs><linearGradient id="flapGrad" x1="0" y1="0" x2="0" y2="1"><stop offset="0" stop-color="#2b2e33"/><stop offset="1" stop-color="#9ca0a6"/></linearGradient></defs>
    <path d="M0 0H502V20Q251 70 0 20Z" fill="url(#flapGrad)"/>
  </svg>
  <div class="wordmark">ZEV COACH</div>
  <svg class="swoosh" viewBox="0 0 502 40" preserveAspectRatio="none">
    <path d="M0 22Q250 8 502 18" stroke="var(--soft-grey)" stroke-width="6" fill="none"/>
    <path d="M0 28Q250 14 502 24" stroke="var(--brand-blue)" stroke-width="3" fill="none"/>
  </svg>
  <div class="address">47 Pemberly Lane, Suite 6, Brookhaven Falls, NY 14099</div>
</section>

<section class="piece letterhead" aria-label="Letterhead">
  <div class="wordmark">ZEV COACH</div>
  <svg class="swoosh" viewBox="0 0 552 40" preserveAspectRatio="none">
    <path d="M0 20Q276 6 552 16" stroke="var(--soft-grey)" stroke-width="6" fill="none"/>
    <path d="M0 26Q276 12 552 22" stroke="var(--brand-blue)" stroke-width="3" fill="none"/>
  </svg>
  <div class="interior-photo" role="img" aria-label="Faint photo of a limo bus interior"></div>
  <div class="footer">
    <div>47 Pemberly Lane, Suite 6, Brookhaven Falls, NY 14099</div>
    <div><span>716-555-0142</span><span>716-555-0187</span><span>866-555-0193</span></div>
    <div><span>tv@zevcoach.com</span><span>www.ZevCoach.com</span></div>
  </div>
</section>

</body>
</html>
```